Buch-Cover für Sonnenherz gesucht
Der Designer hat sich sehr schnell in meine Vorgaben eingearbeitet und gleichzeitig wertvolle Vorschläge zur Optimierung abgegeben. Das Ergebnis ist dadurch sogar besser geworden, als ich mir im Vorfeld ausgemalt hatte. 100% Weiterempfehlung.
Zielgruppe
Wir sind eine Firma die hochwertige Fitnessprodukte produziert und vertreibt. Unsere Zielgruppe sind gesundheitsbewusste Frauen ab Mitte 20 bis open end, die hohe Ansprüche an sich selbst stellen und sich für das Thema Selbstoptimierung interessieren.
Aufgabenstellung
Es soll ein Hardcover gestaltet werden.
Buchtitel: Sonnenherz, Untertitel: Das Erwachen der Seele
Detaillierte Beschreibung der Projektanforderungen siehe Anhang Projektbeschreibung. Darüber hinaus bin ich auch für alternative Gestaltungs-Ideen offen.
Das Design soll der Käuferin folgendes vermitteln:
- Wertigkeit
- Positivität
und sie ein bisschen träumen lassen und natürlich neugierig auf den Inhalt machen.

```html
<!DOCTYPE html>
<html lang="de">
<head>
<meta charset="utf-8">
<title>Sonnenherz – Buchumschlag</title>
<link href="https://fonts.googleapis.com/css2?family=Dancing+Script:wght@600&family=Caveat:wght@400&family=Jost:wght@400&display=swap" rel="stylesheet">
<style>
  :root{
    --gold:#d6b869;
    --lime:#e4e39a;
    --peach:#c9a07c;
    --lavender:#c9b3c6;
    --mist:#d9d4e2;
    --magenta:#c02aa6;
    --ink:#1b1b1b;
    --panel:rgba(255,255,255,0.28);
    --code-box:#e6e6e6;
    --photo-dark:#23263d;
    --photo-mid:#5a6173;
    --photo-warm:#b98a5a;
    --imprint:#b48a1e;
  }
  html,body{margin:0;padding:0;overflow:hidden;}
  body{width:1200px;height:887px;}
  .cover{
    position:relative;width:1200px;height:887px;overflow:hidden;
    background:
      radial-gradient(circle at 78% 20%, var(--lime) 0%, rgba(228,227,154,0) 45%),
      radial-gradient(circle at 20% 8%, var(--peach) 0%, rgba(201,160,124,0) 40%),
      linear-gradient(180deg, var(--gold) 0%, #d8c48c 40%, var(--lavender) 75%, var(--mist) 100%);
  }
  .back-panel{
    position:absolute;left:33px;top:75px;width:489px;height:627px;
    background:var(--panel);border-radius:8px;
  }
  .back-heading{
    position:absolute;left:33px;top:120px;width:489px;margin:0;text-align:center;
    font-family:"Caveat",cursive;font-weight:400;font-size:44px;line-height:54px;color:var(--ink);
  }
  .blurb{
    position:absolute;left:46px;top:204px;width:463px;
    font-family:"Jost",sans-serif;font-size:17.6px;line-height:22.2px;color:var(--ink);
  }
  .blurb p{margin:0 0 22px;text-align:justify;}
  .code-box{
    position:absolute;left:307px;top:714px;width:222px;height:133px;background:var(--code-box);
  }
  .spine-title{
    position:absolute;left:600px;top:216px;transform-origin:0 0;transform:rotate(90deg) translateY(-50%);
    white-space:nowrap;color:var(--ink);
  }
  .spine-title .spine-main{font-family:"Dancing Script",cursive;font-weight:600;font-size:38px;color:var(--magenta);vertical-align:middle;}
  .spine-title .spine-sub{font-family:"Caveat",cursive;font-size:29px;vertical-align:middle;}
  .imprint{
    position:absolute;left:550px;top:812px;width:99px;text-align:center;
    font-family:"Jost",sans-serif;font-size:13px;color:var(--imprint);
  }
  .front-title{
    position:absolute;left:672px;top:170px;width:500px;margin:0;text-align:center;
    font-family:"Dancing Script",cursive;font-weight:600;font-size:98px;line-height:1.1;color:var(--magenta);
    white-space:nowrap;
  }
  .front-subtitle{
    position:absolute;left:672px;top:302px;width:500px;margin:0;text-align:center;
    font-family:"Caveat",cursive;font-weight:400;font-size:32px;line-height:40px;color:var(--ink);
  }
  .cover-photo{
    position:absolute;left:641px;top:480px;width:559px;height:407px;
    background:linear-gradient(160deg, var(--photo-mid) 0%, var(--photo-warm) 45%, var(--photo-dark) 80%);
  }
</style>
</head>
<body>
<div class="cover">
  <div class="back-panel"></div>
  <h2 class="back-heading">« Was zählt wirklich? »</h2>
  <div class="blurb">
    <p>Ich habe mich oft gefragt: Wie soll ich bloß die Liebe und Bestätigung, die mir damals in meiner Kindheit verwehrt blieben, „nachholen“? Lösungsansätze für mein Problem hatte ich in der Vergangenheit durchaus: Ich versuchte das Loch in mir mit Hilfe zur Selbsthilfe, Erfolg im Job und Konsum zu stopfen. Und meine Partner mussten auch für so einiges herhalten.</p>
    <p>Von Gott wollte ich lange nichts wissen. Schließlich hatte er es zugelassen, dass mir sehr viel Unheil in meinem Leben widerfahren ist. Und deshalb war ich echt wütend auf ihn.</p>
    <p>Heutzutage bin ich mir sicher, dass ich mit dieser Denkweise meine Lebenszeit verschwendet habe. Letzten Sommer begriff ich endlich: im Leben gilt die gleiche Gesetzmäßigkeit wie beim Autofahren. Der Rückspiegel ist so klein und die Frontscheibe so groß, weil das, was vor uns liegt, viel wichtiger ist als das, was hinter uns liegt. Aufgrund dieser Erkenntnis entschied ich mich, einen völlig neuen Weg einzuschlagen und wagte mich auf eine spannende Reise, die mein Leben für immer veränderte …</p>
  </div>
  <div class="code-box"></div>

  <div class="spine-title"><span class="spine-main">Sonnenherz</span><span class="spine-sub"> – Das Erwachen der Seele</span></div>
  <div class="imprint">Lichtweg</div>

  <h1 class="front-title">Sonnenherz</h1>
  <p class="front-subtitle">Das Erwachen der Seele</p>
  <div class="cover-photo" role="img" aria-label="Foto: Frau mit Sonnenbrille fährt im offenen Cabrio auf eine sonnige Landstraße zu, Blick durch die Frontscheibe"></div>
</div>
</body>
</html>
```